VC Liquidity Transformation Case Study Design

2-Page VC Case Study Brochure Concept
We are looking for visual design concepts, not finished production files.
This project explores a 2-page institutional brochure for Brisk Harbor Partners that:
Page 1 → Explains our differentiated approach to venture-backed technology exits
Page 2 → Demonstrates how we convert long-tenured portfolio companies into strategic outcomes
The attached Design Guide includes:
• Page wireframe
• Referenced visuals
• Icon direction
• Tone and design rules
Designers should use this as a structural guide, not a constraint.

- BH Process Diagram: several modifications needed to the images to be recreated (various images attached)
- Brisk Harbor Partners 2-Page Brochure small (B1 and Final F1 - psd files) are my current 2 page brochure. Leverage if you'd like.
- Logo package: this is the package of Brisk Harbor Partners logos

Target Market(s)

Institutional capital investors like Venture capitalists and private equity groups

Industry/Entity Type

investment banking

Font styles to use
Sans Serif

Colors
0054AA
0677BA
7BADD7
CADEEF
E8F1F8

Requirements
Must have
• See design guide
Nice to have
• See design guide
Should not have
• See design guide

```html
<!DOCTYPE html>
<html lang="en">
<head>
<meta charset="utf-8">
<title>Brisk Harbor Partners – VC Case Study Brochure</title>
<link rel="stylesheet" href="https://fonts.googleapis.com/css2?family=Open+Sans:wght@300;400;600;700;800&display=swap">
<style>
:root{
  --blue-deep:#0054AA;
  --blue-mid:#0677BA;
  --blue-soft:#7BADD7;
  --blue-pale:#CADEEF;
  --blue-mist:#E8F1F8;
  --navy:#1d4a8c;
  --ink:#1e2a3a;
  --grey-band:#dcdde0;
  --grey-label:#eceef1;
  --stage:#3a3d45;
  --highlight:#fff04a;
}
*{box-sizing:border-box;margin:0;padding:0}
html,body{width:1200px;height:494px;overflow:hidden}
body{background:var(--stage);font-family:"Open Sans",Arial,sans-serif;color:var(--ink);position:relative}
.page{position:absolute;top:14px;width:330px;height:466px;background:#fff;overflow:hidden}
.page--approach{left:258px}
.page--outcome{left:612px}
.page__header{position:absolute;left:0;top:0;width:100%;height:110px;background:linear-gradient(180deg,var(--blue-pale) 0%,var(--blue-mist) 55%,#fff 100%)}
.abs{position:absolute}
.title{position:absolute;left:15px;font-weight:300;color:var(--ink);line-height:1.12}
.title strong{font-weight:700;color:var(--blue-deep)}
.title-rule{position:absolute;height:1.5px;background:var(--blue-deep)}
.tag-box{position:absolute;background:var(--navy);color:#fff;font-weight:600;font-size:6.2px;line-height:1.35;padding:6px 8px}
.label-chip{position:absolute;background:var(--grey-label);font-size:8px;color:var(--ink);text-align:center;line-height:13px;white-space:nowrap;overflow:hidden}
.lens{position:absolute;left:159px;top:107px;width:13px;height:122px;background:var(--grey-label);font-size:7px;writing-mode:vertical-rl;text-align:center;line-height:13px;white-space:nowrap}
.arrow-line{position:absolute;height:1px;background:var(--blue-mid)}
.arrow-line::after{content:"";position:absolute;right:-1px;top:-2px;border-left:4px solid var(--blue-mid);border-top:2.5px solid transparent;border-bottom:2.5px solid transparent}
.stack{position:absolute;left:202px;top:138px;width:108px}
.stack__row{height:22px;font-size:5.6px;line-height:1.2;display:flex;align-items:center;justify-content:flex-end;padding-right:6px;text-align:center}
.stack__row--top{background:linear-gradient(90deg,#c9ccd3,#eef0f3)}
.stack__row--mid{background:linear-gradient(90deg,var(--blue-soft),var(--blue-mist));height:26px}
.stack__row--base{background:linear-gradient(90deg,var(--navy),var(--blue-mid));color:#fff;flex-direction:column;align-items:flex-end;justify-content:center}
.small{font-size:3.6px;display:block}
.quote-band{position:absolute;left:0;top:257px;width:100%;height:47px;background:var(--grey-band);text-align:center;font-size:9.6px;line-height:1.75;padding-top:9px}
.quote-mark{position:absolute;font-size:22px;font-weight:700;color:var(--navy);line-height:1}
.section-heading{position:absolute;font-weight:700;font-size:8px;letter-spacing:.3px;color:var(--navy)}
.lifecycle{position:absolute;left:28px;top:358px;width:290px;height:96px}
.h-title{position:absolute;font-weight:700;color:var(--navy);text-align:center}
.caption{position:absolute;font-size:5.2px;text-align:center;color:var(--ink)}
.italic{font-style:italic;color:#5a6677}
.placeholder{position:absolute;border-radius:3px}
.step{position:absolute;display:flex;align-items:center;gap:4px;font-size:3.8px;font-weight:700;color:var(--navy);line-height:1.2}
.step__icon{width:12px;height:12px;border-radius:50%;border:1.2px solid var(--blue-mid);background:#fff;flex:none}
.highlight{position:absolute;background:var(--highlight);font-weight:700;font-size:4.6px;padding:1px 2px}
.orb{position:absolute;width:42px;height:42px;border-radius:50%;background:radial-gradient(circle at 40% 35%,#fff 0%,var(--blue-mist) 60%,var(--blue-pale) 100%);border:1px solid var(--blue-pale);font-size:2.8px;text-align:center;padding-top:16px;line-height:1.3;font-weight:700;color:var(--navy)}
.orb span{display:block;font-weight:400;color:var(--ink)}
.impact-box{position:absolute;left:189px;top:233px;width:137px;height:106px;border:1px solid #e3e6ea;background:#fff}
.impact-item{position:absolute;top:44px;width:32px;text-align:center;font-size:3.6px;line-height:1.25}
.impact-item svg{display:block;margin:0 auto 3px}
.cta-band{position:absolute;left:0;top:367px;width:100%;height:45px;background:var(--navy);color:#fff;text-align:center;font-size:9.6px;font-weight:600;line-height:1.45;padding-top:9px}
.footer{position:absolute;left:0;top:412px;width:100%;height:54px}
.brand{position:absolute;left:14px;top:19px;display:flex;align-items:center;gap:5px;font-weight:700;font-size:8.6px;color:var(--navy);line-height:1.05}
.brand__dot{width:16px;height:16px;border-radius:50%;background:var(--navy);flex:none}
.footer__rule{position:absolute;top:14px;width:1px;height:28px;background:var(--navy)}
.footer__text{position:absolute;font-size:6.3px;color:var(--ink);line-height:1.55}
</style>
</head>
<body>

<section class="page page--approach">
  <div class="page__header"></div>
  <h1 class="title" style="top:15px;font-size:14px">Unlocking Strategic<br>Value from<br><strong style="font-size:18.5px">Deep Technology</strong></h1>
  <div class="title-rule" style="left:14px;top:75px;width:172px"></div>
  <div class="tag-box" style="left:199px;top:39px;width:131px;height:37px">Helping Venture Investors Transition Long-Held Portfolio Companies into Strategic Outcomes</div>

  <div class="label-chip" style="left:15px;top:108px;width:120px">Traditional Tech I-Banks</div>
  <div class="label-chip" style="left:180px;top:108px;width:144px;font-size:6.6px">Brisk Harbor Partners: IP-Led Approach</div>
  <div class="lens">Signal IP Method LENS</div>

  <svg class="abs" style="left:61px;top:161px" width="34" height="28" viewBox="0 0 34 28" aria-hidden="true">
    <polygon points="4,6 17,2 30,6 17,10" fill="#f2f3f5"/>
    <polygon points="4,6 17,10 17,26 4,22" fill="#d7dade"/>
    <polygon points="17,10 30,6 30,22 17,26" fill="#c4c8ce"/>
  </svg>
  <div class="caption" style="left:20px;top:192px;width:118px;font-size:7.4px">Niche IP Company</div>
  <div class="caption" style="left:20px;top:202px;width:118px;font-size:3.4px">Operations | Sales &amp; Marketing | R&amp;D</div>
  <div class="arrow-line" style="left:115px;top:175px;width:19px"></div>
  <div class="arrow-line" style="left:176px;top:175px;width:19px"></div>

  <div class="stack">
    <div class="stack__row stack__row--top">Signal IP Method</div>
    <div class="stack__row stack__row--mid">Economic Value<br>of Niche IP</div>
    <div class="stack__row stack__row--base"><span style="font-size:5.6px">Niche IP Company</span><span class="small">Operations | Sales &amp; Marketing | R&amp;D</span></div>
  </div>

  <div class="label-chip" style="left:15px;top:226px;width:120px">Value Focus</div>
  <div class="label-chip" style="left:180px;top:226px;width:144px">Value Focus with IP</div>

  <div class="quote-band">Strategic buyers acquire capability acceleration,<br>not revenue history.</div>
  <div class="quote-mark" style="left:62px;top:246px">“</div>
  <div class="quote-mark" style="left:252px;top:284px">”</div>

  <div class="section-heading" style="left:63px;top:316px">VENTURE LIFECYCLE <span style="font-weight:400">POSITIONING</span></div>
  <div class="abs" style="left:63px;top:328px;width:198px;height:1px;background:#d8dbe0"></div>
  <div class="abs" style="left:63px;top:333px;font-size:6.6px;font-weight:600;color:var(--ink)">Unlocking Strategic Value from Deep Technology</div>
  <div class="abs" style="left:63px;top:342px;font-size:4.8px;color:#4a5566">Helping Venture Investors Transition Long-Held Portfolio Companies</div>

  <svg class="lifecycle" viewBox="0 0 290 96" aria-label="Venture lifecycle stages chart">
    <defs>
      <linearGradient id="curveFill" x1="0" x2="1">
        <stop offset="0" stop-color="#E8F1F8"/><stop offset="1" stop-color="#7BADD7"/>
      </linearGradient>
      <linearGradient id="barFill" x1="0" x2="1">
        <stop offset="0" stop-color="#7BADD7"/><stop offset="1" stop-color="#0054AA"/>
      </linearGradient>
    </defs>
    <path d="M0,70 C60,66 110,50 150,36 L150,70 Z" fill="url(#curveFill)" opacity=".6"/>
    <path d="M90,52 C110,44 130,36 155,26" stroke="var(--navy)" stroke-width="2" fill="none"/>
    <polygon points="150,22 158,24 152,30" fill="var(--navy)"/>
    <path d="M186,30 C210,24 235,22 262,24" stroke="#f0a83a" stroke-width="1" stroke-dasharray="2 2" fill="none"/>
    <rect x="98" y="42" width="48" height="30" fill="#7BADD7" opacity=".7"/>
    <rect x="146" y="28" width="40" height="44" fill="#0054AA"/>
    <rect x="140" y="4" width="64" height="10" rx="1" fill="var(--navy)"/>
    <text x="172" y="10.6" font-size="4.3" fill="#fff" text-anchor="middle">Brisk Harbor Engages Here</text>
    <line x1="172" y1="14" x2="172" y2="28" stroke="var(--navy)" stroke-width=".8"/>
    <g fill="var(--blue-mid)"><rect x="14" y="56" width="3" height="6"/><rect x="19" y="52" width="3" height="10"/><rect x="24" y="48" width="3" height="14"/></g>
    <g fill="none" stroke="var(--blue-mid)" stroke-width="1.5"><circle cx="64" cy="54" r="4"/><circle cx="71" cy="57" r="3"/></g>
    <polygon points="122,48 128,58 116,58" fill="none" stroke="#fff" stroke-width="1"/>
    <circle cx="166" cy="42" r="6" fill="none" stroke="#fff" stroke-width="1"/><circle cx="166" cy="42" r="2" fill="#fff"/>
    <rect x="240" y="36" width="16" height="20" rx="6" fill="#d9b25a" role="img" aria-label="Money bag illustration"/>
    <g font-size="4.8" font-weight="600" text-anchor="middle" fill="var(--ink)">
      <text x="20" y="78">EARLY GROWTH</text><text x="66" y="78">SCALING</text><text x="122" y="78">PLATEAU</text>
      <text x="166" y="60" fill="#fff">STRATEGIC</text><text x="166" y="66" fill="#fff">TRANSITION</text>
      <text x="248" y="64">LIQUIDITY</text>
    </g>
    <polygon points="0,83 50,83 54,88 50,93 0,93" fill="#7BADD7"/>
    <polygon points="52,83 140,83 144,88 140,93 52,93" fill="url(#barFill)" opacity=".55"/>
    <polygon points="142,83 210,83 214,88 210,93 142,93" fill="var(--navy)"/>
    <polygon points="212,83 260,83 264,88 260,93 212,93" fill="#7BADD7"/>
    <g font-size="4.4" fill="#fff" text-anchor="middle">
      <text x="24" y="90">EARLY Growth</text><text x="96" y="90" fill="var(--navy)">Strategic</text>
      <text x="176" y="90">Strategic Transition</text><text x="236" y="90">Liquidity</text>
    </g>
  </svg>
</section>

<section class="page page--outcome">
  <div class="page__header"></div>
  <h1 class="title" style="top:17px;font-size:12.5px">From Long-Tenured Holding<br>to <strong style="font-size:15.5px">Strategic Outcome</strong></h1>
  <div class="title-rule" style="left:14px;top:54px;width:198px"></div>
  <div class="tag-box" style="left:223px;top:28px;width:107px;height:28px">How Brisk Harbor Enables Venture Capital Recycling</div>

  <div class="h-title" style="left:0;top:75px;width:180px;font-size:9px">The Challenge</div>
  <div class="caption" style="left:0;top:90px;width:180px;font-size:4.4px">Portfolio Reality</div>
  <div class="placeholder" style="left:14px;top:98px;width:165px;height:100px;background:linear-gradient(180deg,var(--blue-mist),#f4f6f9)" role="img" aria-label="Portfolio reality diagram: traditional focus on two unicorns and three losses versus Brisk Harbor focus on five long-tenured non-unicorns"></div>
  <div class="abs" style="left:181px;top:100px;width:1px;height:112px;background:#c8cdd6"></div>
  <div class="caption" style="left:14px;top:205px;width:165px;font-size:5.2px;line-height:1.5">Capital remains trapped in technically strong<br>but strategically misunderstood platforms.</div>

  <div class="h-title" style="left:182px;top:75px;width:148px;font-size:9px">Brisk Harbor Intervention</div>
  <svg class="abs" style="left:204px;top:91px" width="26" height="26" viewBox="0 0 26 26" aria-hidden="true">
    <circle cx="13" cy="13" r="12" fill="#fff" stroke="var(--blue-mid)" stroke-width="2"/>
    <circle cx="13" cy="13" r="9" fill="var(--blue-mist)"/>
    <text x="13" y="12.5" font-size="2.6" text-anchor="middle" fill="var(--navy)" font-weight="700">SIGNAL IP</text>
    <text x="13" y="15.5" font-size="2.4" text-anchor="middle" fill="var(--navy)">METHOD</text>
  </svg>
  <div class="step" style="left:232px;top:98px">STRATEGIC<br>REFRAMING</div>
  <div class="abs" style="left:216px;top:118px;width:1px;height:60px;background:var(--blue-soft)"></div>
  <div class="step" style="left:210px;top:122px"><span class="step__icon"></span>BUYER<br>MAPPING</div>
  <div class="step" style="left:210px;top:142px"><span class="step__icon"></span>MULTI-<br>RATIONALE<br>POSITIONING</div>
  <div class="step" style="left:210px;top:164px"><span class="step__icon" style="border-radius:2px"></span>STRATEGIC<br>REFRAMING</div>
  <div class="caption italic" style="left:196px;top:185px;width:120px;font-size:3.8px;line-height:1.4">“ Brisk Harbor transforms operating companies<br>into strategic capability platforms. ”</div>

  <div class="h-title" style="left:0;top:230px;width:190px;font-size:8.4px">Process Outcome</div>
  <div class="highlight" style="left:43px;top:247px">Venture outcomes Conclusion 02282026</div>
  <div class="abs" style="left:152px;top:246px;font-size:4px;font-weight:700;color:var(--navy);display:flex;align-items:center;gap:2px"><span style="width:6px;height:6px;border-radius:50%;background:var(--navy);display:inline-block"></span>BRISK HARBOR</div>
  <div class="caption" style="left:14px;top:257px;width:170px;font-size:3.8px;letter-spacing:.2px">BOTTOM SECTION – <b style="color:var(--navy)">IMPACT</b></div>
  <div class="caption" style="left:14px;top:264px;width:170px;font-size:3.6px;font-weight:600">Transforming Plateau Companies Into <span style="color:var(--navy)">Strategic Exits</span> &amp; Recycled Capital</div>

  <div class="orb" style="left:22px;top:272px">PLATEAUED COMPANY<span>Stagnation &amp; Limited Options</span></div>
  <div class="arrow-line" style="left:65px;top:293px;width:7px"></div>
  <div class="orb" style="left:73px;top:272px">BRISK HARBOR ENGAGEMENT<span>Signal IP Method</span></div>
  <div class="arrow-line" style="left:116px;top:293px;width:7px"></div>
  <div class="orb" style="left:124px;top:272px">STRATEGIC EXITS<span>Maximized Value Realized</span></div>

  <div class="abs" style="left:16px;top:321px;font-size:3.4px;font-weight:700">OUTCOMES:</div>
  <div class="abs" style="left:42px;top:318px;width:140px;display:flex;justify-content:space-between;font-size:3px;line-height:1.2">
    <span>● Capital<br>Returned</span><span>● Portfolio<br>Refreshed</span><span>● IP Value<br>Unlocked</span><span>● New Funds /<br>Investments Enabled</span>
  </div>
  <div class="caption" style="left:14px;top:336px;width:170px;font-size:4.2px">Brisk Harbor transforms stagnation into <b style="color:var(--navy)">strategic liquidity.</b></div>

  <div class="impact-box">
    <div class="h-title" style="left:0;top:8px;width:100%;font-size:8.4px">Impact</div>
    <div class="caption" style="left:0;top:21px;width:100%;font-size:4.4px">Outcome</div>
    <div class="impact-item" style="left:5px">
      <svg width="16" height="14" viewBox="0 0 16 14" aria-hidden="true"><g fill="none" stroke="var(--blue-mid)" stroke-width=".8"><circle cx="8" cy="7" r="2"/><circle cx="2" cy="3" r="1.4"/><circle cx="14" cy="3" r="1.4"/><circle cx="3" cy="12" r="1.4"/><circle cx="13" cy="12" r="1.4"/><path d="M3 4 6.5 6M13 4 9.5 6M4 11 7 8.5M12 11 9 8.5"/></g></svg>
      Cross-Sector Buyer Engagement</div>
    <div class="impact-item" style="left:37px">
      <svg width="16" height="14" viewBox="0 0 16 14" aria-hidden="true"><g fill="none" stroke="var(--blue-mid)" stroke-width=".8"><circle cx="8" cy="7" r="6"/><ellipse cx="8" cy="7" rx="2.5" ry="6"/><path d="M2 7h12"/></g></svg>
      A Competitive &amp; Global Process</div>
    <div class="impact-item" style="left:69px">
      <svg width="16" height="14" viewBox="0 0 16 14" aria-hidden="true"><g fill="none" stroke="var(--blue-mid)" stroke-width=".8"><circle cx="8" cy="7" r="6"/><path d="M8 3v4l3 2"/></g></svg>
      Accelerated Closing<br><span style="color:#7a8494">(2–4 mo post LOI)</span></div>
    <div class="impact-item" style="left:101px">
      <svg width="16" height="14" viewBox="0 0 16 14" aria-hidden="true"><g fill="none" stroke="var(--blue-mid)" stroke-width=".8"><path d="M3 9 8 6l5 3-5 3z"/><path d="M3 9v2l5 3 5-3V9"/><path d="M10 5 12 2"/></g></svg>
      Strategic Liquidity</div>
    <div class="caption italic" style="left:0;top:87px;width:100%;font-size:3.8px">Unlocking value from the overlooked majority</div>
  </div>

  <div class="cta-band">Aligning IP-rich companies with strategic demand<br>unlocks liquidity where traditional exits stall.</div>

  <footer class="footer">
    <div class="brand"><span class="brand__dot"></span><span>BRISK HARBOR<br>PARTNERS</span></div>
    <div class="footer__rule" style="left:126px"></div>
    <div class="footer__text" style="left:136px;top:16px">www.briskharborpartners.com<br>hello@briskharborpartners.com</div>
    <div class="footer__rule" style="left:238px"></div>
    <div class="footer__text" style="left:247px;top:12px;font-size:5.8px;line-height:1.45">2200 Meridian Parkway<br>Suite 410,<br>Austin TX 78701</div>
  </footer>
</section>

</body>
</html>
```